Solar energy proposal for homeowners

I am providing households with solar energy proposals, and I need a high-quality brochure that is packaged cleverly to attract the homeowner's attention. Take a look at the one page solar brochure that I have included to get an idea of text and content.

Target Market(s)

Residential Homeowners

Industry/Entity Type

Solar

Requirements
Must have
• High quality document

```html
<!DOCTYPE html>
<html lang="en">
<head>
<meta charset="UTF-8">
<title>Solvane Energy – Solar Flyers</title>
<link href="https://fonts.googleapis.com/css2?family=Barlow+Semi+Condensed:wght@700;800&family=Oswald:wght@500;600&family=Outfit:wght@300;400;500;600&display=swap" rel="stylesheet">
<style>
  :root{
    --stage:#0b3a8c;
    --stage-deep:#06245e;
    --navy:#38416e;
    --ink:#0f4d86;
    --green:#7fd02a;
    --lime:#a6df2c;
    --cyan:#19c3d3;
    --blue:#0b8fd9;
    --teal:#17c2b6;
    --white:#ffffff;
    --text:#2c2f3a;
    --footer-dark:#2a2a2c;
  }
  *{box-sizing:border-box;margin:0;padding:0}
  html,body{width:1200px;height:900px;overflow:hidden}
  body{
    background:radial-gradient(ellipse at 50% 35%,var(--stage) 0%,var(--stage-deep) 100%);
    font-family:"Outfit",sans-serif;color:var(--text);position:relative;
  }
  .flyer{position:absolute;top:54px;width:560px;height:792px;overflow:hidden;box-shadow:0 18px 40px rgba(0,0,0,.35)}
  .flyer--light{left:30px;background:var(--white)}
  .flyer--dark{left:610px;background:var(--navy);color:var(--white)}
  .flyer svg.backdrop{position:absolute;inset:0}
  .abs{position:absolute}

  .brand{font-family:"Outfit",sans-serif;font-weight:400;font-size:24px;color:var(--cyan);display:flex;align-items:center;gap:8px;letter-spacing:.3px}
  .brand__dot{width:18px;height:18px;border-radius:50%;background:var(--cyan)}

  /* light flyer */
  .hero-title{font-family:"Barlow Semi Condensed",sans-serif;font-weight:800;line-height:.9}
  .hero-title__solar{font-size:82px;color:var(--ink);display:block}
  .hero-title__price{font-size:82px;color:var(--green);display:block}
  .hero-title__tag{font-size:21px;color:var(--ink);display:block;margin-top:6px;letter-spacing:-.2px}
  .hero-sub{font-size:15px;color:#1d1d24;line-height:1.2}

  .section-head{font-family:"Oswald",sans-serif;font-weight:600;font-size:26px;line-height:1.05;letter-spacing:-.5px}
  .section-head__accent{color:var(--green)}
  .section-head__base{color:var(--ink)}
  .body-copy{font-size:10.5px;line-height:1.45;color:var(--text)}

  .checklist{list-style:none;font-size:11px;line-height:15px}
  .checklist li{display:flex;align-items:center;gap:10px}
  .checklist li::before{content:"";flex:0 0 auto;width:0;height:0;border-left:8px solid var(--green);border-top:5px solid transparent;border-bottom:5px solid transparent}
  .checklist--dark{line-height:17px}
  .checklist--dark li::before{border-left-color:var(--cyan)}
  .checklist__no{color:var(--cyan)}

  .services{display:flex;flex-direction:column}
  .services-title{font-family:"Oswald",sans-serif;font-weight:600;font-size:27px;line-height:1.1;color:var(--white);letter-spacing:-.6px;white-space:nowrap;margin-bottom:10px}
  .service{display:flex;gap:10px;margin-bottom:9px}
  .service:last-child{margin-bottom:0}
  .service__icon{flex:0 0 26px;height:28px}
  .service__name{font-size:14.5px;font-weight:500;color:var(--cyan);line-height:1.15;white-space:nowrap}
  .service__text{font-size:10px;line-height:1.4;color:var(--white);margin-top:3px}

  .contact-bar{display:flex;align-items:center;justify-content:space-around;font-size:12px;color:var(--white)}
  .contact-bar__item{display:flex;align-items:center;gap:6px;white-space:nowrap}

  /* dark flyer */
  .offer-band{background:linear-gradient(100deg,var(--blue) 0%,var(--cyan) 100%);padding:26px 24px 16px 30px}
  .offer-band__title{font-family:"Barlow Semi Condensed",sans-serif;font-weight:800;font-size:42px;line-height:1;color:var(--white)}
  .offer-band__sub{font-size:15px;line-height:1.2;margin-top:12px;color:var(--white)}
  .dark-head{font-weight:600;font-size:18px;line-height:22px;color:var(--white)}
  .dark-copy{font-size:10.5px;line-height:1.5;color:var(--white);margin-top:6px}
  .dark-service .service__name{font-size:16px}
  .dark-service .service__text{font-size:10.5px}
  .photo{position:absolute}
</style>
</head>
<body>

<!-- Flyer A: light layout -->
<section class="flyer flyer--light">
  <svg class="backdrop" width="560" height="792" viewBox="0 0 560 792">
    <defs>
      <linearGradient id="stripeGrad" x1="0" y1="0" x2="1" y2="0">
        <stop offset="0" stop-color="#0b8fd9"/><stop offset=".55" stop-color="#19c3d3"/><stop offset="1" stop-color="#a6df2c"/>
      </linearGradient>
      <linearGradient id="topStripe" x1="0" y1="1" x2="1" y2="0">
        <stop offset="0" stop-color="#0b8fd9"/><stop offset=".6" stop-color="#19c3d3"/><stop offset="1" stop-color="#7fd02a"/>
      </linearGradient>
      <linearGradient id="photoFade" x1="0" y1="0" x2="1" y2="0">
        <stop offset="0" stop-color="#ffffff"/>
        <stop offset=".35" stop-color="#e9eef3"/>
        <stop offset=".65" stop-color="#c9d6e2"/>
        <stop offset="1" stop-color="#8d99a6"/>
      </linearGradient>
      <linearGradient id="footerGrad" x1="0" y1="0" x2="1" y2="0">
        <stop offset="0" stop-color="#0b8fd9"/><stop offset=".55" stop-color="#19c3d3"/><stop offset="1" stop-color="#a6df2c"/>
      </linearGradient>
    </defs>
    <g role="img" aria-label="Photo: white family house with solar panels on a grey roof against a bright sky">
      <polygon points="0,180 300,0 560,0 560,360 400,298 0,452" fill="url(#photoFade)"/>
    </g>
    <polygon points="0,0 320,0 0,190" fill="var(--navy)"/>
    <polygon points="0,190 320,0 345,0 0,208" fill="url(#topStripe)"/>
    <polygon points="300,356 400,318 540,374 540,792 300,792" fill="var(--navy)"/>
    <polygon points="0,448 400,296 560,360 560,378 400,314 0,466" fill="url(#stripeGrad)"/>
    <polygon points="0,764 560,712 560,792 0,792" fill="url(#footerGrad)"/>
  </svg>

  <div class="brand abs" style="left:30px;top:26px"><span class="brand__dot"></span>Solvane Energy</div>

  <h1 class="hero-title abs" style="left:42px;top:190px">
    <span class="hero-title__solar">SOLAR</span>
    <span class="hero-title__price">FOR $0</span>
    <span class="hero-title__tag">DOWN. NO LIENS. NO KIDDING.</span>
  </h1>
  <p class="hero-sub abs" style="left:44px;top:386px">Power Your Future with<br>Solvane Energy</p>

  <div class="abs" style="left:32px;top:476px;width:258px">
    <h2 class="section-head"><span class="section-head__accent">ABOUT</span> <span class="section-head__base">US</span></h2>
    <p class="body-copy" style="margin-top:5px">At Solvane Energy, our mission is to make solar simple and accessible for everyone. No high-pressure sales-just the information you need to make a smart choice. With our solar rental program, you can lower your monthly energy costs and pay less than your current electricity bill.</p>
  </div>

  <div class="abs" style="left:32px;top:622px;width:258px">
    <h2 class="section-head"><span class="section-head__accent">WHY CHOOSE</span> <span class="section-head__base">US?</span></h2>
    <ul class="checklist" style="margin-top:4px">
      <li>No financing</li><li>No liens</li><li>No down payment</li>
      <li>No insurance costs</li><li>No long-term commitment</li><li>No maintenance costs</li>
    </ul>
  </div>

  <div class="services abs" style="left:312px;top:372px;width:218px">
    <h2 class="services-title">OUR BEST SERVICES</h2>
    <div class="service">
      <svg class="service__icon" viewBox="0 0 28 30"><polygon points="14,1 27,8 27,22 14,29 1,22 1,8" fill="var(--teal)"/><text x="14" y="19" font-size="11" text-anchor="middle" fill="#fff" font-family="Outfit,sans-serif">$</text></svg>
      <div><div class="service__name">Affordable &amp; Transparent</div><p class="service__text">Simple pricing, no hidden fees and a fixed monthly rate lower than typical energy bills</p></div>
    </div>
    <div class="service">
      <svg class="service__icon" viewBox="0 0 28 30"><polygon points="14,1 27,8 27,22 14,29 1,22 1,8" fill="var(--teal)"/><path d="M9 15l4 4 7-8" stroke="#fff" stroke-width="2" fill="none"/></svg>
      <div><div class="service__name">Expert Installation</div><p class="service__text">Certified professionals handle installation, maintenance, and repairs end to end.</p></div>
    </div>
    <div class="service">
      <svg class="service__icon" viewBox="0 0 28 30"><polygon points="14,1 27,8 27,22 14,29 1,22 1,8" fill="var(--teal)"/><path d="M14 8a4 4 0 0 1 4 4c0 3-4 8-4 8s-4-5-4-8a4 4 0 0 1 4-4z" fill="#fff"/></svg>
      <div><div class="service__name">Local Expertise</div><p class="service__text">Florida-based team that understands the needs of Orlando and statewide homeowners</p></div>
    </div>
    <div class="service">
      <svg class="service__icon" viewBox="0 0 28 30"><polygon points="14,1 27,8 27,22 14,29 1,22 1,8" fill="var(--teal)"/><path d="M9 20c0-7 5-10 11-10 0 6-4 10-11 10z" fill="#fff"/></svg>
      <div><div class="service__name">Eco-Friendly</div><p class="service__text">Clean, renewable solar energy that helps reduce your carbon footprint.</p></div>
    </div>
  </div>

  <div class="contact-bar abs" style="left:0;top:764px;width:560px;height:28px">
    <span class="contact-bar__item"><svg width="12" height="12" viewBox="0 0 12 12"><circle cx="6" cy="6" r="6" fill="#fff"/><rect x="4" y="2.5" width="4" height="7" rx="1" fill="var(--blue)"/></svg>(555) 014-2290</span>
    <span class="contact-bar__item"><svg width="12" height="12" viewBox="0 0 12 12"><circle cx="6" cy="6" r="6" fill="#fff"/><circle cx="6" cy="5" r="2" fill="var(--cyan)"/></svg>48 Harbor Lane, Any City</span>
    <span class="contact-bar__item"><svg width="12" height="12" viewBox="0 0 12 12"><circle cx="6" cy="6" r="5" fill="none" stroke="#fff" stroke-width="1.4"/><path d="M1 6h10M6 1v10" stroke="#fff" stroke-width="1"/></svg>www.solvaneenergy.com</span>
  </div>
</section>

<!-- Flyer B: dark layout -->
<section class="flyer flyer--dark">
  <div class="photo" role="img" aria-label="Photo: modern solar-roofed house with a pool and lawn at sunset" style="left:345px;top:0;width:176px;height:396px;background:linear-gradient(180deg,#e9a27a 0%,#c9a6a8 30%,#6f7c8e 55%,#4f6a4a 80%,#3c8fb0 100%)"></div>
  <div class="abs" style="left:521px;top:100px;width:28px;height:250px;background:var(--green)"></div>

  <div class="brand abs" style="left:40px;top:88px;font-size:28px"><span class="brand__dot" style="width:22px;height:22px"></span>Solvane Energy</div>

  <div class="offer-band abs" style="left:22px;top:150px;width:336px">
    <h1 class="offer-band__title">SOLAR FOR $0<br>DOWN.<br>NO LIENS.<br>NO KIDDING.</h1>
    <p class="offer-band__sub">Power Your Future with<br>Solvane Energy</p>
  </div>

  <div class="abs" style="left:40px;top:426px;width:255px">
    <h2 class="dark-head">About Us</h2>
    <p class="dark-copy">At Solvane Energy, our mission is to make solar simple and accessible for everyone. No high-pressure sales-just the information you need to make a smart choice. With our solar rental program, you can lower your monthly energy costs and pay less than your current electricity bill.</p>
  </div>

  <div class="abs" style="left:318px;top:426px;width:222px">
    <h2 class="dark-head">Why Choose Us?</h2>
    <ul class="checklist checklist--dark" style="margin-top:6px;font-size:11px">
      <li><span><span class="checklist__no">No</span> financing</span></li>
      <li><span><span class="checklist__no">No</span> liens</span></li>
      <li><span><span class="checklist__no">No</span> down payment</span></li>
      <li><span><span class="checklist__no">No</span> insurance costs</span></li>
      <li><span><span class="checklist__no">No</span> long-term commitment</span></li>
      <li><span><span class="checklist__no">No</span> maintenance costs</span></li>
    </ul>
  </div>

  <h2 class="dark-head abs" style="left:40px;top:572px">Our Best Services</h2>

  <div class="service dark-service abs" style="left:40px;top:602px;width:255px">
    <svg class="service__icon" viewBox="0 0 28 30"><polygon points="14,1 27,8 27,22 14,29 1,22 1,8" fill="var(--teal)"/><text x="14" y="19" font-size="11" text-anchor="middle" fill="#fff" font-family="Outfit,sans-serif">$</text></svg>
    <div><div class="service__name">Affordable &amp; Transparent</div><p class="service__text">Simple pricing, no hidden fees and a fixed monthly rate lower than typical energy bills</p></div>
  </div>
  <div class="service dark-service abs" style="left:40px;top:672px;width:255px">
    <svg class="service__icon" viewBox="0 0 28 30"><polygon points="14,1 27,8 27,22 14,29 1,22 1,8" fill="var(--teal)"/><path d="M14 8a4 4 0 0 1 4 4c0 3-4 8-4 8s-4-5-4-8a4 4 0 0 1 4-4z" fill="#fff"/></svg>
    <div><div class="service__name">Local Expertise</div><p class="service__text">Florida-based team that understands the needs of Orlando and statewide homeowners</p></div>
  </div>
  <div class="service dark-service abs" style="left:318px;top:582px;width:222px">
    <svg class="service__icon" viewBox="0 0 28 30"><polygon points="14,1 27,8 27,22 14,29 1,22 1,8" fill="var(--teal)"/><path d="M9 15l4 4 7-8" stroke="#fff" stroke-width="2" fill="none"/></svg>
    <div><div class="service__name">Expert Installation</div><p class="service__text">Certified professionals handle installation, maintenance, and repairs end to end.</p></div>
  </div>
  <div class="service dark-service abs" style="left:318px;top:662px;width:222px">
    <svg class="service__icon" viewBox="0 0 28 30"><polygon points="14,1 27,8 27,22 14,29 1,22 1,8" fill="var(--teal)"/><path d="M9 20c0-7 5-10 11-10 0 6-4 10-11 10z" fill="#fff"/></svg>
    <div><div class="service__name">Eco-Friendly</div><p class="service__text">Clean, renewable solar energy that helps reduce your carbon footprint.</p></div>
  </div>

  <div class="contact-bar abs" style="left:0;top:750px;width:560px;height:42px;background:var(--footer-dark)">
    <span class="contact-bar__item"><svg width="12" height="12" viewBox="0 0 12 12"><circle cx="6" cy="6" r="6" fill="#fff"/><rect x="4" y="2.5" width="4" height="7" rx="1" fill="var(--footer-dark)"/></svg>(555) 014-2290</span>
    <span class="contact-bar__item"><svg width="12" height="12" viewBox="0 0 12 12"><circle cx="6" cy="6" r="6" fill="#fff"/><circle cx="6" cy="5" r="2" fill="var(--footer-dark)"/></svg>48 Harbor Lane, Any City</span>
    <span class="contact-bar__item"><svg width="12" height="12" viewBox="0 0 12 12"><circle cx="6" cy="6" r="5" fill="none" stroke="#fff" stroke-width="1.4"/><path d="M1 6h10M6 1v10" stroke="#fff" stroke-width="1"/></svg>www.solvaneenergy.com</span>
  </div>
</section>

</body>
</html>
```